Sightless Fellowship Hall of San Diego needs an ad/flyer for convention program

Established in 1949, the Sightless Fellowship Hall of San Diego's mission is to enrich the lives of blind and visually impaired adults by preparing them for a normal, active life in a society that is principally sighted by encouraging independence.

Located in Harwick Gardens in San Diego, California, we are a nonprofit that gives blind and visually impaired people in our community an opportunity to socialize and interact. We help members build skills, confidence, and self-esteem through our various social, recreational, and educational activities. We were founded partially by Heron Guild members and receive ongoing funding from them.

We need an 8 1/2 by 11 inch color ad in jpg format. We would like it to be editable. This will be the foundation of our rebranding. The ad will be in a meeting program of the California Herons (californiaherons.example) with the goal of highlighting some of our programs in order to solicit donations from individual Heron Guilds, preferably ongoing ones.

We would like the ad to be generic enough that we can use the ad for other events and as a flyer in the future. We want the ad/flyer to be classic but eye popping with color. We want the design to reflect a professional and lively organization that loves to serve our members. We don’t entirely love our logo, but it’s what we have for now. Our next task will be a new logo design.

We would like to highlight some of our programs for our members include bingo, blind waterskiing and surfing, cooking and ceramic classes, foreign language classes, self defense classes, yoga, and craft classes. Many of the crafts our members make are sold during fundraisers, and they include blankets, scarves, beaded animals, and more. See a sampling of pictures. We provide transportation to and from our Center, free lunch while at the Center, and food to take home. Many of these activities continue during the pandemic via online platforms. We are doing monthly home deliveries of food to our members.

We need donations to keep our programs going, and we have building repairs & maintenance that we need donations in order to complete. See attached document regarding donations. Please reach out if you have questions. Thank you.

Web address: sfhsd.example
Street address: The Sightless Fellowship Hall of San Diego, 2716 Merrow St San Diego, CA 92107
Email address: donation@sfhsd.example
To make a donation: https://sfhsd.example/donate-2/

Donors

NonProfit

Sans Serif

Must have
• Highlight programs and information on how to make a donation.
Nice to have
• Information on how much each dollar donated will go - see attachment
Should not have
• Unprofessional or sloppy details

```html
<!DOCTYPE html>
<html lang="en">
<head>
<meta charset="utf-8">
<title>Sightless Fellowship Hall – Donor Flyer</title>
<link href="https://fonts.googleapis.com/css2?family=Arimo:wght@400;700&family=Lato:wght@400;700;900&display=swap" rel="stylesheet">
<style>
:root{
  --red:#e63b3b;
  --orange:#e8962e;
  --green:#2aa57a;
  --purple:#594a9b;
  --heading-purple:#4f3f8e;
  --ink:#1d1d1f;
  --paper:#ffffff;
  --stage:#8e8e8e;
  --pink-tint:#fde9ea;
  --orange-tint:#fdf0dc;
  --green-tint:#e2f3ec;
  --purple-tint:#e8e5f3;
}
*{margin:0;padding:0;box-sizing:border-box}
html,body{width:1200px;height:1200px;overflow:hidden;background:var(--stage)}
body{font-family:"Lato",sans-serif;color:var(--ink)}
.flyer{position:absolute;left:147px;top:18px;width:906px;height:1164px;background:var(--paper);overflow:hidden}
.hero{position:absolute;left:0;top:0;width:906px;height:420px}
.brand{position:absolute;left:700px;top:40px;width:170px;display:flex;align-items:center;gap:10px;font-family:"Lato",sans-serif;font-weight:900;font-size:52px;color:var(--ink);letter-spacing:1px}
.brand-square{width:14px;height:14px;background:var(--ink)}

.section-head{position:absolute;display:flex;align-items:center;gap:16px}
.section-head h2{font-family:"Arimo",sans-serif;font-weight:400;font-size:33px;color:var(--ink);white-space:nowrap}
.section-head h2 strong{font-weight:700;color:var(--heading-purple)}
.know-head{left:28px;top:406px}
.precovid-head{left:487px;top:406px}

.facts{position:absolute;left:50px;top:500px;width:404px;list-style:none}
.fact{position:relative;display:flex}
.fact-marker{position:relative;width:26px;flex:none;display:flex;justify-content:center}
.fact-dot{width:24px;height:24px;border:2px solid #333;border-radius:50%;display:flex;align-items:center;justify-content:center;background:#fff;margin-top:1px}
.fact-dot span{width:12px;height:12px;border-radius:50%}
.fact-line{position:absolute;left:12px;top:33px;width:1.5px;background:#222}
.fact-num{width:40px;flex:none;font-weight:700;font-size:16.5px;padding-left:5px;line-height:21px}
.fact-text{width:338px;font-size:16.5px;line-height:21px;text-align:justify;letter-spacing:0.25px}
.fact-text b{font-weight:700}

.tiers{position:absolute;left:506px;top:500px;width:350px}
.tier-pill{position:absolute;left:0;width:338px;height:29px;border:1.5px solid;border-radius:15px;display:flex;align-items:center;font-size:18.5px;padding-left:3px}
.tier-pill .tick{width:24px;height:24px;border-radius:50%;display:flex;align-items:center;justify-content:center;margin-right:12px}
.tier-list{position:absolute;left:34px;width:313px;list-style:none}
.tier-list li{position:relative;font-size:16.5px;line-height:21px;text-align:justify;margin-bottom:2px}
.tier-list li::before{content:"";position:absolute;left:-18px;top:6px;width:8px;height:8px;border-radius:50%;background:var(--red)}

.pill-red{border-color:var(--red);background:var(--pink-tint)}
.pill-red .tick{background:var(--red)}
.pill-orange{border-color:var(--orange);background:var(--orange-tint)}
.pill-orange .tick{background:var(--orange)}
.pill-green{border-color:var(--green);background:var(--green-tint)}
.pill-green .tick{background:var(--green)}
.pill-purple{border-color:var(--purple);background:var(--purple-tint)}
.pill-purple .tick{background:var(--purple)}

.footer-band{position:absolute;left:0;top:1076px;width:906px;height:64px;background:var(--red);color:#fff;font-size:16.5px;font-weight:700;text-align:center;line-height:21px;padding-top:12px}
.color-strip{position:absolute;left:0;top:1140px;width:906px;height:12px;display:flex}
.color-strip div{flex:1;position:relative}
.strip-dot{position:absolute;top:-1px;width:12px;height:12px;border-radius:50%}
</style>
</head>
<body>
<main class="flyer">

  <svg class="hero" viewBox="0 0 906 420">
    <defs>
      <linearGradient id="yarnTones" x1="0" y1="0" x2="1" y2="1">
        <stop offset="0" stop-color="#8a6fc4"/>
        <stop offset="0.3" stop-color="#f3b6cf"/>
        <stop offset="0.6" stop-color="#f4eef2"/>
        <stop offset="0.8" stop-color="#c89ad0"/>
        <stop offset="1" stop-color="#efe9ea"/>
      </linearGradient>
      <linearGradient id="penguinTones" x1="0" y1="0" x2="0" y2="1">
        <stop offset="0" stop-color="#d9d6d2"/>
        <stop offset="1" stop-color="#8f8f94"/>
      </linearGradient>
      <linearGradient id="angelTones" x1="0" y1="0" x2="0" y2="1">
        <stop offset="0" stop-color="#e6e4e0"/>
        <stop offset="1" stop-color="#3346a8"/>
      </linearGradient>
    </defs>
    <rect x="0" y="0" width="906" height="420" fill="url(#yarnTones)" role="img" aria-label="Photo of stacked hand-knit chunky blankets in purple, blue, pink and white made by members"/>
    <path d="M484,0 C520,125 700,160 906,166 L906,0 Z" fill="var(--paper)"/>
    <path d="M460,0 C500,150 700,205 906,222 L906,166 C700,160 520,125 484,0 Z" fill="var(--orange)"/>
    <path d="M0,190 C150,235 320,300 460,335 C620,365 800,340 906,290 L906,420 L0,420 Z" fill="var(--paper)"/>
    <path d="M0,220 L0,280 C120,300 250,330 330,350 L330,320 C250,290 120,250 0,220 Z" fill="var(--orange)"/>
    <path d="M445,378 C600,385 760,370 820,340 C760,365 600,372 450,362 Z" fill="var(--orange)"/>
    <circle cx="201" cy="290" r="106" fill="var(--paper)"/>
    <circle cx="201" cy="290" r="98" fill="url(#penguinTones)" role="img" aria-label="Photo of a beaded penguin ornament with a Santa hat, handmade by members"/>
    <circle cx="365" cy="326" r="86" fill="var(--paper)"/>
    <circle cx="365" cy="326" r="79" fill="url(#angelTones)" role="img" aria-label="Photo of a beaded angel ornament in blue and clear beads"/>
  </svg>

  <div class="brand" aria-label="Sightless Fellowship Hall"><span class="brand-square"></span>SFH</div>

  <header class="section-head know-head">
    <svg width="76" height="84" viewBox="0 0 76 84">
      <circle cx="34" cy="42" r="33" fill="#fff" stroke="#eee" stroke-width="1"/>
      <circle cx="34" cy="42" r="36" fill="none" stroke="var(--red)" stroke-width="5" stroke-dasharray="42 300" transform="rotate(-90 34 42)"/>
      <circle cx="34" cy="42" r="36" fill="none" stroke="var(--orange)" stroke-width="5" stroke-dasharray="0 46 40 300" transform="rotate(-90 34 42)"/>
      <circle cx="34" cy="42" r="36" fill="none" stroke="var(--green)" stroke-width="5" stroke-dasharray="0 90 30 300" transform="rotate(-90 34 42)"/>
      <circle cx="34" cy="42" r="36" fill="none" stroke="var(--purple)" stroke-width="5" stroke-dasharray="0 124 28 300" transform="rotate(-90 34 42)"/>
      <circle cx="34" cy="42" r="14" fill="none" stroke="#222" stroke-width="1.6"/>
      <text x="34" y="48" font-family="Arimo, sans-serif" font-size="17" text-anchor="middle" fill="#222">?</text>
    </svg>
    <h2>Did you <strong>know?</strong></h2>
  </header>

  <header class="section-head precovid-head">
    <svg width="76" height="84" viewBox="0 0 76 84">
      <circle cx="34" cy="42" r="33" fill="#fff" stroke="#eee" stroke-width="1"/>
      <circle cx="34" cy="42" r="36" fill="none" stroke="var(--red)" stroke-width="5" stroke-dasharray="42 300" transform="rotate(-90 34 42)"/>
      <circle cx="34" cy="42" r="36" fill="none" stroke="var(--orange)" stroke-width="5" stroke-dasharray="0 46 40 300" transform="rotate(-90 34 42)"/>
      <circle cx="34" cy="42" r="36" fill="none" stroke="var(--green)" stroke-width="5" stroke-dasharray="0 90 30 300" transform="rotate(-90 34 42)"/>
      <circle cx="34" cy="42" r="36" fill="none" stroke="var(--purple)" stroke-width="5" stroke-dasharray="0 124 28 300" transform="rotate(-90 34 42)"/>
      <path d="M34,36 C30,30 24,33 27,38 L34,44 L41,38 C44,33 38,30 34,36 Z" fill="none" stroke="#222" stroke-width="1.6"/>
      <path d="M20,52 L28,48 L40,50 C43,51 42,54 39,54 L32,54 M20,58 L30,60 L46,52" fill="none" stroke="#222" stroke-width="1.6" stroke-linecap="round"/>
    </svg>
    <h2>Pre-<strong>Covid:</strong></h2>
  </header>

  <ol class="facts">
    <li class="fact" style="margin-bottom:21px">
      <div class="fact-marker"><div class="fact-dot"><span style="background:var(--red)"></span></div><div class="fact-line" style="height:74px"></div></div>
      <div class="fact-num">1.</div>
      <p class="fact-text">During the pandemic we offer Bingo, Trivia and other virtual games every week, where blind and low vision participants can win SFH bucks. <b>You can sponsor one day of games for $35.</b></p>
    </li>
    <li class="fact" style="margin-bottom:21px">
      <div class="fact-marker"><div class="fact-dot"><span style="background:var(--orange)"></span></div><div class="fact-line" style="height:120px"></div></div>
      <div class="fact-num">2.</div>
      <p class="fact-text">You can provide 75 gift bags for our ‘We are in This Together’ home delivery program. Many of our blind and low vision people are isolated and stuck at home. These gift packages are welcomed with enthusiasm and gratefulness. Your rewards are huge smiles and happy faces.</p>
    </li>
    <li class="fact" style="margin-bottom:20px">
      <div class="fact-marker"><div class="fact-dot"><span style="background:var(--green)"></span></div><div class="fact-line" style="height:20px"></div></div>
      <div class="fact-num">3.</div>
      <p class="fact-text">Our building is over 20 years old and requires ongoing maintenance and repairs</p>
    </li>
    <li class="fact" style="margin-bottom:20px">
      <div class="fact-marker"><div class="fact-dot"><span style="background:var(--purple)"></span></div><div class="fact-line" style="height:40px"></div></div>
      <div class="fact-num">4.</div>
      <p class="fact-text"><b>Fencing (cage) required to protect outside air conditioning units from vandalism. Cost: $2,500</b></p>
    </li>
    <li class="fact">
      <div class="fact-marker"><div class="fact-dot"><span style="background:var(--red)"></span></div></div>
      <div class="fact-num">5.</div>
      <p class="fact-text">Wanted: Sponsors for weekly virtual bingo and trivia games: Blind and Low vision participants receive one SFH buck per win. SFH bucks are turned into gift cards and Bayline transportation passes. <b>Sponsor one week for $40. Sponsor 1 month for $160</b></p>
    </li>
  </ol>

  <section class="tiers">
    <div class="tier-pill pill-red" style="top:5px"><span class="tick"><svg width="16" height="16" viewBox="0 0 16 16"><circle cx="8" cy="8" r="6.5" fill="none" stroke="#fff" stroke-width="1.3"/><path d="M5,8 L7.3,10.3 L11.5,5.5" fill="none" stroke="#fff" stroke-width="1.5"/></svg></span>$10 per month or $120 will buy:</div>
    <ul class="tier-list" style="top:47px">
      <li>60 meals for our lunch program – we serve 130 meals each week</li>
      <li>13 round trip Bayline transportation tickets</li>
      <li>Enough beads to make 35 Rosalie angels in our craft class</li>
    </ul>

    <div class="tier-pill pill-orange" style="top:188px"><span class="tick"><svg width="16" height="16" viewBox="0 0 16 16"><circle cx="8" cy="8" r="6.5" fill="none" stroke="#fff" stroke-width="1.3"/><path d="M5,8 L7.3,10.3 L11.5,5.5" fill="none" stroke="#fff" stroke-width="1.5"/></svg></span>$20 per month or $240 will buy:</div>
    <ul class="tier-list" style="top:230px">
      <li>26 round trip Bayline transportation tickets</li>
      <li>One month of large print and Braille translation newsletter printing</li>
    </ul>

    <div class="tier-pill pill-green" style="top:328px"><span class="tick"><svg width="16" height="16" viewBox="0 0 16 16"><circle cx="8" cy="8" r="6.5" fill="none" stroke="#fff" stroke-width="1.3"/><path d="M5,8 L7.3,10.3 L11.5,5.5" fill="none" stroke="#fff" stroke-width="1.5"/></svg></span>$50 per month or $600 will buy:</div>
    <ul class="tier-list" style="top:370px">
      <li>300 lunches</li>
      <li>Thanksgiving dinner with all the fixings for 80 to 100 guests</li>
    </ul>

    <div class="tier-pill pill-purple" style="top:470px"><span class="tick"><svg width="16" height="16" viewBox="0 0 16 16"><circle cx="8" cy="8" r="6.5" fill="none" stroke="#fff" stroke-width="1.3"/><path d="M5,8 L7.3,10.3 L11.5,5.5" fill="none" stroke="#fff" stroke-width="1.5"/></svg></span>$100 per month or $1200 will buy:</div>
    <ul class="tier-list" style="top:512px">
      <li>Approximately 10 Bingo parties including food and prizes</li>
    </ul>
  </section>

  <footer class="footer-band">
    <p>$1,083 per month or $13,000 per year will fund our entire lunch program for the year.</p>
    <p>Every dollar donated goes to support SFH participants and programs.</p>
  </footer>
  <div class="color-strip">
    <div style="background:#f9c9c9"></div>
    <div style="background:#fbdcae"><span class="strip-dot" style="left:-6px;background:#f3a98a"></span></div>
    <div style="background:#bfe5d6"><span class="strip-dot" style="left:-6px;background:#c9d9a6"></span></div>
    <div style="background:#bcc1e8"><span class="strip-dot" style="left:-6px;background:#8fb0c6"></span></div>
  </div>

</main>
</body>
</html>
```